Innovative Inbox Lantern Pop ups

Overview:
We’re creating a library of popup templates for our Cartwell app, Inbox Lantern (https://inboxlantern.example/
). These templates will be available for store owners across all types of businesses to use right away.

Most popup templates online are generic boxes with text and a button. That’s exactly what we don’t want. We want you to create out-of-the-box, design-driven templates that are instantly eye-catching, memorable, and conversion-focused.

Think of these as blank canvases: your designs should be so creative that store owners from any niche (fashion, tech, food, fitness, etc.) can drop in their own text, titles, and images — and still stand out.

What to Design:

5 unique popup templates (desktop + mobile).

Must work for any type of business and support any headline/title.

Templates should be bold, unexpected, and visually differentiated from competitors like Quorl, Varemix, Nebo, and Flickbinder.

Include clear CTA areas (sign up, shop now, claim discount, etc.).

Designs should be mobile-first but also adapt beautifully to desktop.

Creative Direction:

Avoid standard box layouts — think beyond the rectangle.

Explore gamification, storytelling, interactive feel.

Use bold typography, unusual shapes, layered visuals, playful patterns, or luxury minimalism — but always in a way that supports conversions.

These are templates, not ads, so keep the text editable and layout flexible.

Deliverables:

Source files (Figma, Adobe XD, or Sketch).

Editable layers so text/images can be swapped easily.

5 designs with both desktop and mobile versions.

Contest Details:

This is a ArtTroupe contest. Multiple designers will submit entries.

We’ll select 1 winner based on creativity, originality, and differentiation.

The winning designs will become part of our client-facing template library.

Tips for Winning:

Design for universality: any store should be able to use your template by swapping in their own title/offer.

Be bold, surprising, and innovative. If your design looks like a typical popup, it won’t win.

Think of a popup as a mini-experience — something users remember, not ignore.
Updates

Hello Designers,

We have revised the project requirements, as it appears the client is not achieving the expected results. Please note that this project is not for logo design but for creating Inbox Lantern pop-ups. I have uploaded a sample image to the project brief for your reference. Kindly focus on producing innovative designs and avoid copying the sample provided to prevent any copyright concerns.

If you have any questions regarding the project, please feel free to reach out to the client through the discussion board.

Requirements
Should not have
• This is NOT a Logo Design.

```html
<!DOCTYPE html>
<html lang="en">
<head>
<meta charset="utf-8">
<title>Inbox Lantern popup templates</title>
<link rel="stylesheet" href="https://fonts.googleapis.com/css2?family=Montserrat:wght@700;800&family=Poppins:wght@400;500;700;800&display=swap">
<style>
  :root {
    --canvas: #c8c8c8;
    --white: #ffffff;
    --ink: #000000;
    --fit-blue: #5b8ad9;
    --fit-blue-deep: #2f5aa0;
    --fit-line: #3e5f9e;
    --fit-navy: #3a4a78;
    --fit-bg: #eef1f5;
    --shoe-bg: #3d3f44;
    --shoe-orange: #e07f24;
    --shoe-yellow: #f4b43c;
    --shoe-red: #c0301a;
    --fruit-bg: #201c20;
    --fruit-cyan: #22bfdc;
    --fruit-wave: #5fe0ec;
  }
  * { margin: 0; padding: 0; box-sizing: border-box; }
  html, body { width: 838px; height: 1200px; overflow: hidden; background: var(--canvas); }
  .board { position: relative; width: 838px; height: 1200px; }
  .popup {
    position: absolute; left: 29.3px; width: 1500px; height: 700px;
    transform: scale(0.5236); transform-origin: 0 0; overflow: hidden;
  }
  .popup--fitness { top: 27.2px; background: linear-gradient(90deg, #e6e9ee, var(--fit-bg) 50%, #f5f6f8); }
  .popup--shoes { top: 416.8px; }
  .popup--fruit { top: 804.2px; }
  .layer { position: absolute; inset: 0; width: 1500px; height: 700px; }
  .photo { position: absolute; }
  .copy {
    position: absolute; left: 0; width: 1500px; text-align: center;
    color: var(--white); line-height: 1; white-space: nowrap;
  }
  .display { font-family: "Montserrat", sans-serif; font-weight: 700; letter-spacing: 1px; }
  .display--heavy { font-weight: 800; }
  .body { font-family: "Poppins", sans-serif; font-weight: 400; }
  .cta { position: absolute; width: 236px; height: 54px; }
  .cta::before {
    content: ""; position: absolute; left: 6px; top: -8px; width: 238px; height: 56px;
    border: 2px solid var(--white); border-radius: 8px;
  }
  .cta span {
    position: absolute; inset: 0; background: var(--ink); border-radius: 8px;
    color: var(--white); font-family: "Poppins", sans-serif; font-weight: 700; font-size: 17px;
    display: flex; align-items: center; justify-content: center; letter-spacing: 0.2px;
  }
  .offer-strong { font-weight: 700; }
  .underline { border-bottom: 2px solid var(--white); padding-bottom: 2px; }
</style>
</head>
<body>
<main class="board">

  <!-- Fitness popup -->
  <section class="popup popup--fitness">
    <div class="photo" role="img" aria-label="Athletic woman in a black sports top, hand on hip" style="left:1100px;top:0;width:400px;height:700px;background:linear-gradient(90deg,rgba(176,122,90,0) 0%,#b5805f 30%,#9c6a4e 60%,#2b2727 85%);border-radius:180px 0 0 0;"></div>
    <svg class="layer" viewBox="0 0 1500 700" aria-hidden="true">
      <circle cx="289" cy="87" r="43" fill="#4a7fd6"/>
      <g stroke="var(--fit-line)" stroke-width="8" stroke-linecap="round" fill="none">
        <line x1="627" y1="22" x2="755" y2="22"/>
        <line x1="797" y1="22" x2="839" y2="22"/>
        <line x1="406" y1="660" x2="536" y2="660"/>
        <line x1="570" y1="662" x2="602" y2="662"/>
        <line x1="638" y1="660" x2="673" y2="662"/>
        <line x1="300" y1="180" x2="292" y2="258"/>
        <line x1="290" y1="298" x2="285" y2="352"/>
        <line x1="276" y1="410" x2="264" y2="536"/>
      </g>
      <path d="M300 600 L365 110 Q372 57 430 57 L1120 52 Q1170 52 1176 110" fill="none" stroke="var(--fit-line)" stroke-width="4"/>
      <path d="M360 125 L430 125 L370 630 L320 630 Q285 630 290 590 Z" fill="var(--fit-blue-deep)"/>
      <path d="M470 81 L1150 81 Q1185 81 1178 116 L1080 600 Q1066 630 1034 630 L330 630 Q298 630 304 598 L395 116 Q402 81 470 81 Z" fill="var(--fit-blue)"/>
      <path d="M1186 70 Q1222 80 1218 110 Q1214 130 1222 145" fill="none" stroke="var(--fit-navy)" stroke-width="13" stroke-linecap="round"/>
      <line x1="1124" y1="438" x2="1102" y2="568" stroke="var(--fit-line)" stroke-width="7" stroke-linecap="round"/>
      <g fill="#4a7fd6">
        <path d="M1170 244 L1182 262 L1158 262 Z"/>
        <path d="M1166 268 L1178 286 L1154 286 Z"/>
        <path d="M1162 292 L1174 310 L1150 310 Z"/>
        <path d="M1158 316 L1170 334 L1146 334 Z"/>
        <path d="M1154 340 L1166 358 L1142 358 Z"/>
      </g>
      <g fill="none" stroke="#4a7fd6" stroke-width="3">
        <path d="M799 686 L823 664 L847 686 L871 664 L895 686 L919 664 L943 686 L967 674"/>
        <path d="M805 692 L829 670 L853 692 L877 670 L901 692 L925 670 L949 692 L971 680"/>
      </g>
    </svg>
    <div class="photo" role="img" aria-label="Fitness couple holding dumbbells" style="left:304px;top:353px;width:210px;height:277px;background:linear-gradient(180deg,#8a6a58,#3a3a40 55%,#2a2a30);border-radius:90px 90px 0 0;"></div>
    <p class="copy display" style="top:200px;left:-8px;font-size:34px;">TRANSFORM YOUR FITNESS</p>
    <p class="copy display display--heavy" style="top:260px;left:-8px;font-size:50px;letter-spacing:2px;">JOURNEY TODAY!</p>
    <p class="copy body" style="top:336px;left:-11px;font-size:30px;">Get Your First Month at <span class="offer-strong underline" style="font-size:38px;">50% Off!</span></p>
    <p class="copy body" style="top:386px;left:-11px;font-size:30px;">Limited Time Only.</p>
    <a class="cta" style="left:615px;top:465px;"><span>CLAIM MY DISCOUNT</span></a>
  </section>

  <!-- Shoe popup -->
  <section class="popup popup--shoes">
    <div class="photo" role="img" aria-label="Rows of leather boots and shoes seen from above" style="inset:0;background:linear-gradient(180deg,#2f3034,#4a4b50 50%,#35363a),var(--shoe-bg);"></div>
    <svg class="layer" viewBox="0 0 1500 700" aria-hidden="true">
      <path d="M744 152 L1004 112 Q1150 100 1215 195" fill="none" stroke="var(--shoe-red)" stroke-width="4"/>
      <path d="M454 119 Q600 125 760 150 L1160 160 Q1270 200 1268 340 Q1262 450 1160 540 Q1100 590 1040 589 L400 560 Q240 540 218 420 Q210 360 250 320 Q330 170 454 119 Z" fill="var(--shoe-yellow)"/>
      <path d="M370 153 L1180 152 Q1262 170 1262 310 Q1262 420 1180 490 Q1120 545 1060 555 L330 556 Q240 556 228 470 Q220 380 250 260 Q290 160 370 153 Z" fill="var(--shoe-orange)" opacity="0.96"/>
      <path d="M262 505 Q300 600 404 612 L744 554" fill="none" stroke="var(--shoe-red)" stroke-width="4"/>
    </svg>
    <p class="copy display display--heavy" style="top:238px;left:6px;font-size:65px;letter-spacing:3px;">STEP INTO STYLE</p>
    <p class="copy body" style="top:318px;left:-6px;font-size:34px;">Sign up today &amp;</p>
    <p class="copy body" style="top:364px;left:-6px;font-size:34px;">get <span style="font-weight:800;font-size:44px;">15% off</span> your first pair.</p>
    <a class="cta" style="left:630px;top:444px;"><span>CLAIM MY DISCOUNT</span></a>
  </section>

  <!-- Fruit popup -->
  <section class="popup popup--fruit">
    <div class="photo" role="img" aria-label="Illustrated pattern of citrus slices, kiwis, strawberries and leaves on dark ground" style="inset:0;background:radial-gradient(circle at 85% 45%,#c98a2a 0,rgba(201,138,42,0) 22%),radial-gradient(circle at 20% 70%,#a8333a 0,rgba(168,51,58,0) 20%),radial-gradient(circle at 35% 75%,#5f7a3a 0,rgba(95,122,58,0) 18%),radial-gradient(circle at 20% 15%,#b86a30 0,rgba(184,106,48,0) 18%),var(--fruit-bg);"></div>
    <div class="photo" role="img" aria-label="Pile of watermelon, bananas, grapes and strawberries" style="left:507px;top:4px;width:512px;height:200px;background:radial-gradient(ellipse at 50% 75%,#e0b530 0,#6f8f2c 35%,#b62a36 55%,#3c3670 75%,rgba(60,54,112,0) 100%);border-radius:50% 50% 10% 10%;"></div>
    <svg class="layer" viewBox="0 0 1500 700" aria-hidden="true">
      <path d="M524 178 Q560 160 600 182 Q640 200 680 186 Q720 172 760 190 Q800 202 840 188 Q880 176 920 194 Q960 204 1024 190 L1024 640 Q1024 654 1010 654 L538 654 Q524 654 524 640 Z" fill="var(--fruit-cyan)"/>
      <path d="M700 192 Q760 172 820 194 Q880 182 940 198 Q990 190 1024 194 L1024 207 Q960 198 900 212 Q840 198 780 208 Q730 204 700 192 Z" fill="var(--fruit-wave)"/>
    </svg>
    <p class="copy display" style="top:292px;left:26px;font-size:37px;">FRESH, JUICY FRUITS</p>
    <p class="copy display" style="top:346px;left:26px;font-size:28px;">DELIVERED TO YOUR HOME!</p>
    <p class="copy body" style="top:398px;left:26px;font-size:44px;">Get 15% Off</p>
    <p class="copy body" style="top:452px;left:26px;font-size:26px;">Your First Order of Fresh Fruits!</p>
    <a class="cta" style="left:653px;top:529px;"><span>CLAIM MY DISCOUNT</span></a>
  </section>

</main>
</body>
</html>
```